Logo and 2 card faces for a card-based party game

I'm launching a party game on Fundhollow soon and would like to get a more professional design for the cards and game. The game is about crushing other people's dreams and superpowers, so a clean and fun look is important. The game is titled Wrangleberry (learn more about the game here: https://www.boardloomworks.com/games/wrangleberry) and includes two types of cards that I'd like you to design both front and back. The first type is the Wrangleberry cards that have 4 categories to choose from on each card face. I'd like a symbol for each of the 4 categories: superpower, occupation, lifetime supply, and fulfilled dream. I'm thinking maybe a bucket with a list in front of it for fulfilled dream, an infinity symbol on a packaging box for lifetime supply, a lightning bolt or something more creative (generic superhero emblem) for a superpower, and maybe a fireman's hat or something else that represents a job or occupation. There will be text going next to the symbols on the card face (see examples of the old design on the URL provided above or in the attached files), so just copy the text from any of those cards to make sure it fits. For the card back, I'd like you to design a logo for Wrangleberry. You could incorporate any of the following ideas: The word Wrangleberry being crushed in a vice or shattered by a gavel. The logo is the only thing needed for the back of the card, but please add a border, color, texture, etc. to make it look professional. The second type of card is the bonus point cards (examples of the old design can also be found at the URL provided above or in the attached files). The same logo could be placed on the back of these cards with something to make them stand out as bonus point cards instead of Wrangleberry cards (a color change, text, or whatever looks good). The face of the bonus point cards will need space for text (as seen in the old design), but has room for your creativity as well. Do whatever fits with the theme set by the Wrangleberry cards and make it look clean, fun, and professional. Here are a couple of inspiration pieces of design that I like for card games: https://www.fundhollow.com/projects/brenvoltis/quibbletons https://www.fundhollow.com/projects/marcopelindry/snap-fizzle-the-party-game-of-sudden-answers If you win this contest, it is very likely that I will work with you one on one for additional needs, including design of the box for the game and an instructions booklet. Thank you!

Here's some of the feedback I provided to a submission that I thought might be helpful for all to see:

1. I'd prefer if the front of the card didn't prioritize one category over the others. All the same size would be ideal. I like the idea of the symbols and text being on banners, sort of like the Snap Fizzle example link that I posted, although other ideas are welcome.

2. A design element that runs throughout the game and ties the front and back of the card together would be nice. Whether you use banners, a similar border, gradients, vector graphics, or whatever else is open to your design interpretation and expertise.

3. For the logo, I'd really like to see the name Wrangleberry being hit with a gavel or in something similar to a car crusher machine where it looks like it's being smashed.

Target Market(s)

20-30 year olds. College students and young professionals. Male and female. Enjoy social get-togethers, "hanging out", etc. Play drinking games, charades, and other party games.

Industry/Entity Type

Games

Requirements
Must have
• Full bleed on the poker-sized cards so that printer errors are minimized.
Nice to have
• The logo can be horizontal or vertical on the card back, but should match the direction of the text on the card face. Any creativity you can bring to the logo/card back that matches the theme of the game (crushing dreams, superpowers, jobs, etc.) is appreciated.
Should not have
• The bird that is in the old design. I'm moving on from that amateur look.

```html
<!DOCTYPE html>
<html lang="en">
<head>
<meta charset="utf-8">
<title>Wrangleberry – Logo and Card Faces</title>
<link rel="stylesheet" href="https://fonts.googleapis.com/css2?family=Francois+One&family=Nunito:wght@600;700&display=swap">
<style>
  :root {
    --page: #ffffff;
    --sun-light: #fff8cf;
    --sun-mid: #fde98a;
    --sun-edge: #fbd95a;
    --brand-red: #c8231e;
    --badge-orange: #f4a53a;
    --red: #d3302a;
    --green: #2f8a3a;
    --green-dark: #1d6a2a;
    --green-light: #6bb54a;
    --blue: #1f64ae;
    --navy: #27317a;
    --purple: #7b3596;
    --purple-light: #9c4fb5;
    --orange-deep: #f08a1c;
    --orange-light: #fbc044;
    --ink: #1e1e1e;
    --white: #ffffff;
    --star: #f6b51f;
  }
  * { box-sizing: border-box; margin: 0; padding: 0; }
  html, body { width: 1200px; height: 785px; overflow: hidden; background: var(--page); }
  .sheet { position: relative; width: 1200px; height: 785px; }

  .logo-text {
    font-family: "Francois One", sans-serif;
    color: var(--brand-red);
    letter-spacing: 0.5px;
    line-height: 1;
    text-transform: none;
  }
  .main-logo {
    position: absolute; left: 100px; top: 145px; width: 310px;
    text-align: center; font-size: 56px;
  }

  .card {
    position: absolute; width: 272px; height: 194px;
    border-radius: 6px; overflow: hidden;
  }
  .sunburst { background: radial-gradient(circle at 50% 50%, var(--sun-light) 0%, var(--sun-mid) 60%, var(--sun-edge) 100%); }
  .bonus-back { background: radial-gradient(circle at 50% 45%, var(--orange-light) 0%, var(--orange-deep) 100%); }

  .card-back-logo {
    position: absolute; left: 0; right: 0; top: 78px; text-align: center; font-size: 38px;
  }

  /* category card */
  .category {
    position: absolute; left: 40px; width: 196px; height: 32px;
    clip-path: polygon(0 8%, 100% 0, 98% 100%, 2% 92%);
    color: var(--white); font-family: "Nunito", sans-serif; font-weight: 700;
    font-size: 12.5px; display: flex; align-items: center; justify-content: center;
  }
  .category--red { top: 20px; background: var(--red); }
  .category--green { top: 58px; background: var(--green); }
  .category--blue { top: 96px; background: var(--blue); }
  .category--purple { top: 134px; background: var(--purple); }
  .category-icon {
    position: absolute; width: 36px; height: 36px; border-radius: 50%;
    border: 3px solid var(--star);
  }
  .category-icon--red { left: 36px; top: 18px; background: var(--red); }
  .category-icon--green { left: 202px; top: 56px; background: var(--green); }
  .category-icon--blue { left: 36px; top: 94px; background: var(--blue); }
  .category-icon--purple { left: 202px; top: 132px; background: var(--purple); }

  /* badges */
  .badge {
    position: absolute; left: 59px; top: 20px; width: 154px; height: 154px; border-radius: 50%;
  }
  .badge--red { background: radial-gradient(circle, var(--star) 0%, var(--red) 45%, var(--red) 62%, var(--badge-orange) 64%); }
  .badge--green { background: radial-gradient(circle, var(--star) 0%, var(--green) 45%, var(--green) 62%, var(--badge-orange) 64%); }
  .badge--purple { background: radial-gradient(circle, var(--star) 0%, var(--purple) 45%, var(--purple) 62%, var(--badge-orange) 64%); }
  .badge--navy { background: radial-gradient(circle, var(--star) 0%, var(--navy) 45%, var(--navy) 62%, var(--badge-orange) 64%); }
  .badge--small { left: 71px; top: 22px; width: 130px; height: 130px; }

  .band {
    position: absolute; left: 32px; width: 208px; height: 40px;
    clip-path: polygon(0 20%, 100% 0, 94% 50%, 100% 100%, 0 80%, 6% 50%);
    font-family: "Francois One", sans-serif; color: var(--white);
    display: flex; align-items: center; justify-content: center;
    font-size: 24px; letter-spacing: 1px;
  }
  .band--red { top: 104px; background: var(--red); }
  .band--green { top: 84px; background: var(--green); font-size: 20px; }
  .band--purple { top: 88px; background: var(--purple); font-size: 20px; }
  .band--navy { top: 84px; background: var(--blue); font-size: 20px; }
  .band--bonus-back { top: 122px; left: 58px; width: 156px; height: 36px; background: var(--red); }
  .bonus-back-logo { top: 72px; font-size: 34px; }

  .badge-caption {
    position: absolute; left: 0; right: 0; top: 160px; text-align: center;
    font-family: "Nunito", sans-serif; font-weight: 600; font-size: 12.5px; color: var(--ink);
  }

  /* award cards */
  .award { padding: 10px; }
  .award--green { background: linear-gradient(135deg, var(--green-light), var(--green-dark)); }
  .award--blue { background: linear-gradient(135deg, var(--navy), var(--blue)); }
  .award--purple { background: linear-gradient(135deg, var(--purple), var(--purple-light)); }
  .award-panel {
    width: 100%; height: 100%; background: var(--white); border-radius: 5px;
    display: flex; flex-direction: column; align-items: center; padding-top: 14px;
    font-family: "Nunito", sans-serif; font-weight: 600; color: var(--ink);
    font-size: 12.5px; line-height: 1.25; text-align: center;
  }
  .award-logo { font-size: 20px; margin-bottom: 10px; }
  .award-title {
    font-family: "Francois One", sans-serif; font-size: 32px; line-height: 1.05;
    display: flex; align-items: center; gap: 12px; margin: 2px 0 4px;
  }
  .award-title--green { color: var(--green); }
  .award-title--blue { color: var(--navy); }
  .award-title--purple { color: var(--purple); margin: 0 0 6px; }
  .star { width: 22px; height: 22px; fill: var(--star); }
</style>
</head>
<body>
<main class="sheet">

  <div class="main-logo logo-text">Wrangleberry</div>

  <section class="card sunburst" style="left:448px; top:72px;">
    <div class="card-back-logo logo-text">Wrangleberry</div>
  </section>

  <section class="card sunburst" style="left:754px; top:72px;">
    <div class="category category--red">I can read minds!</div>
    <div class="category category--green">Gift cards!</div>
    <div class="category category--blue">Tour Guide!</div>
    <div class="category category--purple">Win a gold medal!</div>
    <div class="category-icon category-icon--red" role="img" aria-label="Superpower symbol"></div>
    <div class="category-icon category-icon--green" role="img" aria-label="Lifetime supply symbol"></div>
    <div class="category-icon category-icon--blue" role="img" aria-label="Occupation symbol"></div>
    <div class="category-icon category-icon--purple" role="img" aria-label="Fulfilled dream symbol"></div>
  </section>

  <section class="card sunburst" style="left:36px; top:311px;">
    <div class="badge badge--red" role="img" aria-label="Star emblem badge"></div>
    <div class="band band--red">BONUS</div>
  </section>

  <section class="card award award--green" style="left:321px; top:311px;">
    <div class="award-panel">
      <div class="award-logo logo-text">Wrangleberry</div>
      <p>Award this card to the player<br>who wrote the most</p>
      <div class="award-title award-title--green">
        <svg class="star" viewBox="0 0 24 24"><polygon points="12,1 15,9 23,9 16.5,14 19,22 12,17 5,22 7.5,14 1,9 9,9"/></svg>
        OFFENSIVE
        <svg class="star" viewBox="0 0 24 24"><polygon points="12,1 15,9 23,9 16.5,14 19,22 12,17 5,22 7.5,14 1,9 9,9"/></svg>
      </div>
      <p>stipulation!</p>
    </div>
  </section>

  <section class="card bonus-back" style="left:607px; top:311px;">
    <div class="card-back-logo bonus-back-logo logo-text">Wrangleberry</div>
    <div class="band band--bonus-back">BONUS</div>
  </section>

  <section class="card sunburst" style="left:892px; top:311px;">
    <div class="badge badge--green" role="img" aria-label="Star emblem badge"></div>
    <div class="band band--green" style="top:100px;">OFFENSIVE</div>
  </section>

  <section class="card award award--blue" style="left:36px; top:518px;">
    <div class="award-panel">
      <div class="award-logo logo-text">Wrangleberry</div>
      <p>Award this card to the player<br>who wrote the most</p>
      <div class="award-title award-title--blue">
        <svg class="star" viewBox="0 0 24 24"><polygon points="12,1 15,9 23,9 16.5,14 19,22 12,17 5,22 7.5,14 1,9 9,9"/></svg>
        FUNNIEST
        <svg class="star" viewBox="0 0 24 24"><polygon points="12,1 15,9 23,9 16.5,14 19,22 12,17 5,22 7.5,14 1,9 9,9"/></svg>
      </div>
      <p>stipulation!</p>
    </div>
  </section>

  <section class="card award award--purple" style="left:321px; top:518px;">
    <div class="award-panel">
      <div class="award-logo logo-text">Wrangleberry</div>
      <div class="award-title award-title--purple">
        <svg class="star" viewBox="0 0 24 24"><polygon points="12,1 15,9 23,9 16.5,14 19,22 12,17 5,22 7.5,14 1,9 9,9"/></svg>
        RUNNER UP
        <svg class="star" viewBox="0 0 24 24"><polygon points="12,1 15,9 23,9 16.5,14 19,22 12,17 5,22 7.5,14 1,9 9,9"/></svg>
      </div>
      <p>Award this card to the player<br>who wrote the second-least-<br>desirable stipulation!</p>
    </div>
  </section>

  <section class="card sunburst" style="left:607px; top:518px;">
    <div class="badge badge--purple badge--small" role="img" aria-label="Star emblem badge"></div>
    <div class="band band--purple">RUNNER UP</div>
    <p class="badge-caption">The second-least-desirable</p>
  </section>

  <section class="card sunburst" style="left:892px; top:518px;">
    <div class="badge badge--navy" role="img" aria-label="Star emblem badge"></div>
    <div class="band band--navy" style="top:100px;">FUNNIEST</div>
  </section>

</main>
</body>
</html>
```